DL Flyer and magnet design

I am in need of a new flyer design to show some offers on each side. First side Water filtration. Second side Heat pump hot water. I will attach an existing design from a previous flyer/magnet. I have also got some information to go on the flyer and images/logo.

Side 1: Water Filtration Solutions
Coral Ridge Pipeworks and Heating
Fresh, Clean Water for Every Tap

Water Filtration Solutions
1️⃣ High Flow Water Filtration
Starting from just $550!

2️⃣ Whole House Water Filtration
Enjoy pure water throughout your home – starting from $1800!

3️⃣ Whole House Water Filtration with UV Lamp (Perfect for rainwater systems)
Get the ultimate filtration – starting from $3000!

🎁 FREE BRAVO COOLER
With every water filtration system or referral!

📞 Call us today: 0491 837 254
🌐 Visit our website: www.coralridgeph.example.au

💧 Better water, better life. Call now for a free quote!

Side 2: Heat Pump Hot Water Systems
Energy-Efficient Hot Water Solutions

Heat Pump Hot Water Systems
🌟 Rebates Available!
Save big with government incentives on energy-efficient hot water systems.

💼 All Major Makes, Models, and Sizes
We supply and install trusted brands to suit your household’s needs.

💳 Interest-Free Finance Options
Upgrade now and pay later with flexible payment plans.

🎁 FREE BRAVO COOLER
With every heat pump system or referral!

💧 Upgrade to energy-efficient hot water and save!

Please include on the flyer. Valid until 30/6/2-25 Images are for illustrative purposes only and may not represent the exact product or service provided

```html
<!DOCTYPE html>
<html lang="en">
<head>
<meta charset="utf-8">
<title>Coral Ridge Pipeworks and Heating – DL Flyers</title>
<link href="https://fonts.googleapis.com/css2?family=Audiowide&family=Poppins:ital,wght@0,400;0,500;0,600;0,700;1,700&display=swap" rel="stylesheet">
<style>
  :root{
    --orange:#f26b26;
    --blue:#2f3490;
    --blue-dark:#2a2a78;
    --red:#e5423a;
    --white:#ffffff;
    --backdrop:#6d6e72;
  }
  *{box-sizing:border-box;margin:0;padding:0}
  html,body{width:1200px;height:844px;overflow:hidden;background:var(--backdrop)}
  body{position:relative;font-family:"Poppins",sans-serif;color:var(--white)}
  .flyer{position:absolute;top:109px;width:483px;height:625px;overflow:hidden}
  .flyer--water{left:88px;background:var(--blue)}
  .flyer--heat{left:629px;background:var(--orange)}
  .photo{position:absolute;left:0;top:0;width:483px;height:330px}
  .flyer--water .photo{background:linear-gradient(160deg,#6fcdf0 0%,#cfe9d8 30%,#e6e8e4 50%,#6fa64a 80%,#4f8a32 100%)}
  .flyer--heat .photo{background:linear-gradient(150deg,#d9dcdf 0%,#eeeff0 35%,#3f9bd8 65%,#c84a36 90%)}
  .shapes{position:absolute;inset:0;width:483px;height:625px}
  .corner-title{position:absolute;font-weight:700;font-style:italic;font-size:17px;line-height:16px;text-transform:uppercase;color:var(--white)}
  .flyer--water .corner-title{left:22px;top:26px;transform:rotate(-22deg);text-align:center}
  .flyer--heat .corner-title{left:355px;top:18px;transform:rotate(24deg);text-align:left}
  .brand-panel{position:absolute;left:0;width:285px;height:81px;background:rgba(255,255,255,.9);border-radius:0 24px 24px 0;display:flex;align-items:center;gap:9px;padding-left:18px}
  .flyer--water .brand-panel{top:129px}
  .flyer--heat .brand-panel{top:71px}
  .brand-square{width:34px;height:34px;background:var(--orange);flex:none}
  .brand-name{font-weight:600;font-size:17px;line-height:19px;color:var(--blue)}
  .validity{position:absolute;top:252px;font-weight:700;font-style:italic;font-size:13px;line-height:14px}
  .flyer--water .validity{left:389px;color:var(--orange)}
  .flyer--heat .validity{left:25px;color:var(--blue)}
  .disclaimer{position:absolute;top:225px;width:245px;font-size:4.6px;white-space:nowrap;transform-origin:0 0;transform:rotate(-90deg)}
  .flyer--water .disclaimer{left:466px;top:470px}
  .flyer--heat .disclaimer{left:468px;top:485px}
  .headline{position:absolute;left:40px;font-family:"Audiowide",sans-serif;font-size:18px;line-height:22px;text-transform:uppercase;color:var(--white)}
  .flyer--water .headline{top:342px}
  .flyer--heat .headline{top:329px}
  .divider{position:absolute;width:1px}
  .flyer--water .divider{left:156px;top:338px;height:142px;background:var(--orange)}
  .flyer--heat .divider{left:174px;top:324px;height:142px;background:var(--blue)}
  .offers{position:absolute;font-size:10.6px;line-height:12.4px;list-style:none}
  .flyer--water .offers{left:186px;top:335px;width:290px}
  .flyer--heat .offers{left:197px;top:322px;width:270px}
  .offers li{margin-bottom:7px}
  .flyer--water .accent{color:var(--orange)}
  .flyer--heat .accent{color:var(--blue)}
  .slogan{position:absolute;font-weight:700;font-size:17px;line-height:16px}
  .flyer--water .slogan{left:12px;top:578px}
  .contact{position:absolute;top:563px}
  .flyer--water .contact{left:296px}
  .flyer--heat .contact{left:25px}
  .contact-prompt{font-size:11px;line-height:13px}
  .contact-phone{font-weight:700;font-size:27px;line-height:28px;letter-spacing:.3px}
  .contact-web{font-size:10.6px;line-height:11px}
  .closing{position:absolute;left:293px;top:590px;font-size:13px;line-height:15px}
</style>
</head>
<body>

<section class="flyer flyer--water" aria-label="Water filtration flyer">
  <div class="photo" role="img" aria-label="Photo of a reverse osmosis water filter system standing in green grass"></div>
  <svg class="shapes" viewBox="0 0 483 625" aria-hidden="true">
    <path fill="var(--orange)" d="M0 0H280C200 20 140 55 95 82C62 100 30 106 0 104Z"/>
    <path fill="var(--orange)" d="M0 247C40 238 90 268 140 293C200 320 262 306 330 260C390 220 432 188 483 203V625H0Z"/>
    <path fill="var(--blue)" d="M0 255C40 246 90 276 140 301C200 328 262 314 330 268C390 228 432 196 483 211V625H0Z"/>
    <path fill="var(--blue-dark)" d="M0 478C50 458 120 500 190 545C250 582 330 570 483 478V625H0Z"/>
    <path fill="var(--orange)" d="M0 545C60 520 110 560 180 590C230 610 272 600 322 570C382 535 432 492 483 492V625H0Z"/>
  </svg>
  <h2 class="corner-title">Water<br>Filtration<br>Solutions</h2>
  <div class="brand-panel"><span class="brand-square"></span><span class="brand-name">Coral Ridge Pipeworks<br>and Heating</span></div>
  <p class="validity">Valid until<br>30/6/2-25</p>
  <p class="disclaimer">Images are for illustrative purposes only and may not represent the exact product or service provided</p>
  <h1 class="headline">Fresh<br>Clean<br>Water<br>For<br>Every<br>Tap</h1>
  <span class="divider"></span>
  <ul class="offers">
    <li>High Flow Water Filtration<br>Starting from just <span class="accent">$550!</span></li>
    <li>Whole House Water Filtration<br>Enjoy pure water throughout your home<br>Starting from <span class="accent">$1800!</span></li>
    <li>Whole House Water Filtration with UV Lamp<br>(Perfect for rainwater systems)<br>Get the ultimate filtration – starting from <span class="accent">$3000!</span></li>
    <li><span class="accent">FREE BRAVO COOLER</span> With every water filtration<br>system or <span class="accent">referral!</span></li>
  </ul>
  <p class="slogan">Better water<br>Better life.</p>
  <div class="contact">
    <p class="contact-prompt">Call now for a free quote!</p>
    <p class="contact-phone">0491 837 254</p>
    <p class="contact-web">www.coralridgeph.example.au</p>
  </div>
</section>

<section class="flyer flyer--heat" aria-label="Heat pump hot water flyer">
  <div class="photo" role="img" aria-label="Photo of a plant room with blue and red hot water tanks and insulated pipes"></div>
  <svg class="shapes" viewBox="0 0 483 625" aria-hidden="true">
    <path fill="var(--blue)" d="M483 0H200C262 22 318 78 380 100C422 112 455 106 483 98Z"/>
    <path fill="var(--blue)" d="M0 195C50 178 100 208 160 248C222 290 282 318 342 298C402 278 440 242 483 256V625H0Z"/>
    <path fill="var(--orange)" d="M0 203C50 186 100 216 160 256C222 298 282 326 342 306C402 286 440 250 483 264V625H0Z"/>
    <path fill="var(--red)" d="M110 520C200 495 300 560 400 520C440 504 465 490 483 490V570C420 580 350 585 290 578Z"/>
    <path fill="var(--blue)" d="M0 500C50 478 100 500 160 540C222 580 290 600 483 560V625H0Z"/>
  </svg>
  <h2 class="corner-title">Heat Pump<br>Hot Water<br>Systems</h2>
  <div class="brand-panel"><span class="brand-square"></span><span class="brand-name">Coral Ridge Pipeworks<br>and Heating</span></div>
  <p class="validity">Valid until<br>30/6/2-25</p>
  <p class="disclaimer">Images are for illustrative purposes only and may not represent the exact product or service provided</p>
  <h1 class="headline">Heat<br>Pump<br>Hot<br>Water<br>Systems</h1>
  <span class="divider"></span>
  <ul class="offers">
    <li>Coral Ridge Pipeworks and Heating<br>Energy-Efficient Hot Water Solutions</li>
    <li><span class="accent">Rebates Available!</span><br>Save big with government incentives on energy-efficient hot water systems.</li>
    <li>All Major Makes, Models, and Sizes<br>We supply and install trusted brands to suit your household’s needs.</li>
    <li><span class="accent">Interest-Free Finance Options</span><br>Upgrade now and pay later with flexible payment plans.</li>
    <li style="margin-top:12px"><span class="accent">FREE BRAVO COOLER</span><br>With every heat pump system or referral!</li>
  </ul>
  <div class="contact">
    <p class="contact-prompt">Call now for a free quote!</p>
    <p class="contact-phone">0491 837 254</p>
    <p class="contact-web">www.coralridgeph.example.au</p>
  </div>
  <p class="closing">Upgrade to energy-efficient<br>hot water and save!</p>
</section>

</body>
</html>
```